Company's Core Values to be on our Office Walls

We are a biotechnology consulting company in Massachusetts with about 40 employees. Please check out quelvo.com for our look and more information on our business.

We have 4 core values in the company which we would like to display in our office. (Could be on our walls, could be placed in our website, could be placed anywhere. - We would like a multi-use for this graphic but PRIMARILY on our walls.)
No measurements involved yet, hence we'd like the source file to enable us to stretch the graphics. What's important is to see the designs in this contest.

Design: Looking for a wall display - decal, glass board, vinyl (we're open)
- of our Core Values to have in our reception. We want a Double-Helix
incorporated as the core values are "in our DNA" like the one attached
(would like to see some designs with the exact photo and some used as
inspiration for a unique creative design). Open to various sizes, we have a
few different walls we could place them on.

We are looking for a creative Core Value display to have in our new office. We want a sleek, out of the box design!

Quelvo's 4 Core Values are:
> Put Others First
> Have the Courage to Take Action
> Take Personal Responsibility
> Have fun!
***We welcome any infographics per core value. We are open to your creativity!

**WE WANT THE ACTUAL CORE VALUES ON DISPLAY**
We already have a brand (attached).
Need our actual values on display in office.
We want the actual values on the wall, our logo can be incorporated but not
necessarily.

Overview of company: Young consulting firm for biotech and pharmaceuticals
in the Greater Boston area. We are service based, our employees are
engineers and specialists that work on our clients site. Company was
established in 2010, we moved into our New England office 3 months ago!

Colors: Our main color is blue but we also use orange, green, purple, and
teal. See quelvo.com for our colors.

Target Market(s)

New Hires and Clients - We want to impress them!
Employees and clients - we want employees inspired by the core
values and clients to be impressed by them/separate us from the competition.

Industry/Entity Type

Biotechnology

Font styles to use
Sans Serif

Colors

Designer to choose colors to be used in the design.

Requirements
Must have
• Creativity!
• Some sort of tie to science/biotech
• Color - Blue is our company color but would like others as well. See website for brand colors.

```html
<!DOCTYPE html>
<html lang="en">
<head>
<meta charset="utf-8">
<title>Quelvo Core Values</title>
<link rel="stylesheet" href="https://fonts.googleapis.com/css2?family=Arimo:wght@400;700&display=swap">
<style>
  :root {
    --ink: #1c4e6e;
    --ink-text: #1f5a7a;
    --helix-light: #2a93c4;
    --helix-dark: #134a6b;
    --bg-center: #ffffff;
    --bg-edge: #e6e7e8;
    --line: #2f6f93;
  }
  * { box-sizing: border-box; margin: 0; padding: 0; }
  html, body { width: 1200px; height: 1199px; overflow: hidden; }
  body {
    font-family: "Arimo", Arial, sans-serif;
    background: radial-gradient(circle at 55% 45%, var(--bg-center) 0%, var(--bg-edge) 70%);
    position: relative;
  }
  .helix {
    position: absolute;
    left: 72px; top: 54px;
    width: 360px; height: 1086px;
    border-radius: 40px;
    background: linear-gradient(90deg, var(--helix-dark), var(--helix-light) 50%, var(--helix-dark));
    opacity: .9;
  }
  .connectors { position: absolute; left: 0; top: 0; }
  .node-label {
    position: absolute;
    font-size: 16px; font-weight: 700;
    color: var(--ink);
  }
  .value-card {
    position: absolute;
    left: 644px; width: 446px; height: 180px;
    border: 3px solid var(--ink);
    border-radius: 32px;
    display: flex; align-items: center;
    padding-left: 18px;
  }
  .value-icon { width: 160px; height: 110px; flex: none; }
  .value-text {
    flex: 1;
    text-align: center;
    font-size: 35px; line-height: 1.2;
    color: var(--ink-text);
    padding-right: 14px;
  }
  .icon-fill { fill: var(--ink); }
  .icon-stroke { fill: none; stroke: var(--ink); stroke-width: 6; }
  .fun-mark { width: 160px; height: 110px; display: flex; align-items: center; }
  .fun-mark span {
    display: block; width: 90px; height: 90px; border-radius: 50%;
    background: linear-gradient(135deg, #2a6a8e, var(--ink));
  }
</style>
</head>
<body>
  <div class="helix" role="img" aria-label="Blue double-helix DNA strand running down the left side"></div>

  <svg class="connectors" width="1200" height="1199" viewBox="0 0 1200 1199" aria-hidden="true">
    <g stroke="var(--line)" stroke-width="2">
      <line x1="472" y1="146" x2="644" y2="146"/>
      <line x1="472" y1="450" x2="644" y2="450"/>
      <line x1="472" y1="752" x2="644" y2="752"/>
      <line x1="462" y1="1040" x2="644" y2="1040"/>
    </g>
    <g fill="var(--ink)">
      <circle cx="472" cy="146" r="12"/>
      <circle cx="472" cy="450" r="12"/>
      <circle cx="472" cy="752" r="12"/>
      <circle cx="462" cy="1040" r="12"/>
    </g>
  </svg>
  <div class="node-label" style="left:492px;top:120px">Quelvo</div>
  <div class="node-label" style="left:492px;top:424px">Quelvo</div>
  <div class="node-label" style="left:492px;top:726px">Quelvo</div>
  <div class="node-label" style="left:482px;top:1014px">Quelvo</div>

  <div class="value-card" style="top:60px">
    <svg class="value-icon" viewBox="0 0 160 110" aria-hidden="true">
      <circle class="icon-stroke" cx="30" cy="38" r="13"/>
      <path class="icon-stroke" d="M8 78 q0-24 22-24 q22 0 22 24"/>
      <circle class="icon-stroke" cx="58" cy="30" r="14"/>
      <path class="icon-stroke" d="M36 72 q0-26 22-26 q24 0 24 26"/>
      <path class="icon-stroke" d="M30 84 q10 20 30 10"/>
      <path class="icon-fill" d="M52 80 l12 -4 l-4 14 z"/>
      <text x="88" y="78" font-family="Arimo, Arial, sans-serif" font-weight="700" font-size="46" fill="var(--ink)">1</text>
      <text x="114" y="58" font-family="Arimo, Arial, sans-serif" font-weight="700" font-size="24" fill="var(--ink)">st</text>
    </svg>
    <div class="value-text">Put Others<br>First</div>
  </div>

  <div class="value-card" style="top:356px">
    <svg class="value-icon" viewBox="0 0 160 110" aria-hidden="true">
      <circle class="icon-stroke" cx="28" cy="30" r="16" stroke-dasharray="5 3"/>
      <circle class="icon-stroke" cx="34" cy="78" r="20" stroke-dasharray="6 3"/>
      <circle class="icon-stroke" cx="90" cy="44" r="34" stroke-dasharray="7 3"/>
      <circle class="icon-fill" cx="90" cy="44" r="22"/>
    </svg>
    <div class="value-text">Have the<br>Courage to<br>Take Action</div>
  </div>

  <div class="value-card" style="top:654px">
    <svg class="value-icon" viewBox="0 0 160 110" aria-hidden="true">
      <circle class="icon-stroke" cx="30" cy="36" r="17"/>
      <path class="icon-stroke" d="M4 96 q0-38 26-38 q26 0 26 38"/>
      <circle class="icon-stroke" cx="100" cy="52" r="34"/>
      <rect class="icon-fill" x="90" y="30" width="26" height="12" rx="2" transform="rotate(-30 103 36)"/>
      <rect class="icon-fill" x="96" y="40" width="6" height="28" transform="rotate(-30 99 54)"/>
      <rect class="icon-fill" x="78" y="70" width="34" height="7" rx="1"/>
    </svg>
    <div class="value-text">Take<br>Personal<br>Responsibility</div>
  </div>

  <div class="value-card" style="top:948px">
    <div class="fun-mark" role="img" aria-label="Playful round game-character icon"><span></span></div>
    <div class="value-text">Have fun!</div>
  </div>
</body>
</html>
```